Business Card Design for Mabel's Pantry

We make food for dogs.
Business Card Design (using the logo designed by you). Our Brand color is a bright canary yellow. For example our signage is predominantly yellow, with the logo in black. I'd like the card also to use that imagery.
Feel free to use the two sides creatively.
Vertical Design is also great.

Industry/Entity Type

Pet food

Contact Information for Business Card

Name, email, website, phone no

Font styles to use
Sans Serif

Colors
59FF00
82FF00
B8FF75
E3FFCB
F4FFEA
FFF300
FFF600
FEFA6F
FFFEC7
FFFEE8

Requirements
Nice to have
• A graphic in the same brush stroke style of the logo shoeing a doggy bowl of food

```html
<!DOCTYPE html>
<html lang="en">
<head>
<meta charset="utf-8">
<title>Mabel's Pantry – Business Card</title>
<link href="https://fonts.googleapis.com/css2?family=Montserrat:wght@600;700&family=Raleway:wght@400;500&display=swap" rel="stylesheet">
<style>
  :root {
    --page: #ffffff;
    --stage: #e4e5e7;
    --card: #fee155;
    --ink: #111111;
    --ink-soft: #333333;
  }
  * { margin: 0; padding: 0; box-sizing: border-box; }
  html, body {
    width: 1200px; height: 1020px; overflow: hidden;
    background: var(--page);
    position: relative;
  }
  .stage {
    position: absolute; left: 35px; top: 37px;
    width: 1130px; height: 968px;
    background: var(--stage);
  }
  .card {
    position: absolute; top: 75px;
    width: 503px; height: 880px;
    background: var(--card);
    border-radius: 30px;
    box-shadow: 0 6px 22px rgba(0,0,0,0.18);
  }
  .card--front { left: 75px; }
  .card--back { left: 634px; }

  .brand {
    position: absolute; left: 0; width: 100%;
    display: flex; flex-direction: column; align-items: center;
  }
  .brand__dot {
    width: 96px; height: 96px; border-radius: 50%;
    background: var(--ink);
    margin-bottom: 36px;
  }
  .brand__name {
    font-family: 'Montserrat', sans-serif;
    font-weight: 700;
    font-size: 44px;
    line-height: 50px;
    color: var(--ink);
    white-space: nowrap;
  }
  .card--front .brand { top: 132px; }
  .card--back .brand { top: 344px; }

  .person {
    position: absolute; top: 458px; left: 0; width: 100%;
    text-align: center; color: var(--ink-soft);
  }
  .person__name {
    font-family: 'Montserrat', sans-serif;
    font-weight: 700; font-size: 40px; letter-spacing: -1.5px;
    line-height: 44px;
  }
  .person__role {
    font-family: 'Raleway', sans-serif;
    font-weight: 500; font-size: 23px; letter-spacing: 1px;
    line-height: 28px;
    margin-top: 2px;
  }

  .icon-row {
    position: absolute; top: 549px; left: 71px; width: 333px; height: 35px;
    display: flex; align-items: center; justify-content: center; gap: 6px;
  }
  .icon-row__rule { flex: 1; height: 2px; background: var(--ink-soft); }
  .icon-row__rule:first-child { margin-right: 4px; }
  .icon-row__rule:last-child { margin-left: 8px; }
  .icon {
    width: 31px; height: 35px; border-radius: 3px;
    background: var(--ink-soft);
    display: flex; align-items: center; justify-content: center;
  }

  .contact {
    position: absolute; top: 606px; left: 0; width: 100%;
    text-align: center;
    font-family: 'Raleway', sans-serif; font-weight: 400;
    font-size: 23px; line-height: 35px; color: var(--ink-soft);
  }
  .contact__divider {
    position: absolute; top: 722px; left: 92px; width: 292px; height: 2px;
    background: var(--ink-soft);
  }
  .address {
    position: absolute; top: 735px; left: 0; width: 100%;
    text-align: center;
    font-family: 'Raleway', sans-serif; font-weight: 400;
    font-size: 24px; line-height: 34px; color: var(--ink-soft);
  }
</style>
</head>
<body>
  <div class="stage"></div>

  <section class="card card--front">
    <div class="brand">
      <div class="brand__dot"></div>
      <div class="brand__name">MABEL'S PANTRY</div>
    </div>

    <div class="person">
      <div class="person__name">DANIEL CARTER</div>
      <div class="person__role">Managing Director</div>
    </div>

    <div class="icon-row">
      <span class="icon-row__rule"></span>
      <span class="icon" aria-label="Phone">
        <svg width="20" height="20" viewBox="0 0 24 24"><path fill="#fee155" d="M6.6 10.8a15.5 15.5 0 0 0 6.6 6.6l2.2-2.2c.3-.3.7-.4 1-.2 1.1.4 2.3.6 3.6.6.6 0 1 .4 1 1V20c0 .6-.4 1-1 1C10.6 21 3 13.4 3 4c0-.6.4-1 1-1h3.5c.6 0 1 .4 1 1 0 1.3.2 2.5.6 3.6.1.3 0 .7-.2 1z"/></svg>
      </span>
      <span class="icon" aria-label="Email">
        <svg width="22" height="18" viewBox="0 0 24 18"><rect x="1" y="1" width="22" height="16" fill="none" stroke="#fee155" stroke-width="1.8"/><path d="M1 1l11 9 11-9M1 17l8-7M23 17l-8-7" fill="none" stroke="#fee155" stroke-width="1.5"/></svg>
      </span>
      <span class="icon" aria-label="Website">
        <svg width="22" height="22" viewBox="0 0 24 24"><circle cx="12" cy="12" r="10" fill="none" stroke="#fee155" stroke-width="2"/><path d="M2 12h20M12 2c3 3 3 17 0 20M12 2c-3 3-3 17 0 20" fill="none" stroke="#fee155" stroke-width="1.5"/></svg>
      </span>
      <span class="icon-row__rule"></span>
    </div>

    <div class="contact">
      <div>044-987 321 650</div>
      <div>hello@mabelpantry.com</div>
      <div>www.mabelpantry.com</div>
    </div>
    <div class="contact__divider"></div>
    <div class="address">
      <div>57, Orchard Lane West</div>
      <div>Fairview City, 30418</div>
    </div>
  </section>

  <section class="card card--back">
    <div class="brand">
      <div class="brand__dot"></div>
      <div class="brand__name">MABEL'S PANTRY</div>
    </div>
  </section>
</body>
</html>
```